Wine labels Velmora Wine Council - Nueva etiqueta El Consejo Regulador de vinos de Albarrán

Velmora Wines Council, based in southern Spain, are looking to create a new suite of wine labels which retain the elegance of the Velmora Wines industry while reinvigorating their image to the modern era and a new generation of Sherry Wine lovers. These labels will be used across the Velmora Wines Council's range of wines for the promotion of the Velmora Wines industry.

Your design must present at least two styles of Velmora Wines which demonstrate an elegant, modern interpretation and understanding of the unique mood and personality for these wines and the essence of southern Spain.

10 labels will be created based on the winning design, one for each of the unique varieties of Velmora Wines within the collection. This collection comprises of several different wine varieties including: Fino, Manzanilla, Amontillado, Oloroso, Palo Cortado, Medium, Cream, Pale Cream, Pedro Ximenez and Moscatel.

We recommend you visit our website www.velmora-vinos.example/wines as the source to understanding the origins and unique personality of these diverse wines.

El Consejo Regulador de los Vinos de Albarrán y Tordesal quiere renovar las etiquetas de los vinos utilizados para sus actividades de promoción genérica. Esta colección de vinos comprende las tipologías más importantes de la región que incluye: fino, manzanilla, amontillado, oloroso, palo cortado, pale cream, medium, cream, pedro ximénez y moscatel. Por lo tanto se precisan 10 etiquetas, una para cada uno de los vinos mencionados.
Updates

Project Deadline Extended
Reason: Due to some confusion with the deadline we wish to officially extend the deadline to allow designers one last week to submit their entries.

Target Market(s)

Industry, journalists, media, sommeliers, chefs, wine writers

Industry/Entity Type

Council

Requirements
Must have
• Front and Back label plus capsule:
• Front label can have either of the two official logos of the Velmora Wine council titled Vinos de Albarrán Digital or not, this is optional. Must include: Vino selecionado por el Consejo Regulador de la Denominacion de Origen, Name of the variety of wine eg FINO, percentage of alcohol eg 15% and quantity 75 cl.
• The back of the label must include the council logo titled Sellora and 4 additional logos positioned smaller. The Europa logo must appear larger than the 3 other logos. Space for descriptive text about the wine is also required.
• The dimensions of the bottle can be found at this link http://www.vidrialto.example/es/catalogo/vinos-y-espumosos/bordelesas/bd-orla
• Altura:305 mm
• Diámetro base:76,20 mm
• Diámetro hombro:82 mm
• Tipo boca:Cetie
• Peso:750 gr
• Capacidad:75 cl
• Etiqueta delantera y trasera y capsula
• La etiqueta delantera puede incluir el logo oficial del Consejo Regulador o el logo digital, o ninguno, esto es opcional. Debe incluir el siguiete texto: Vino selecionado por el Consejo Regulador de la Denominacion de Origen, el nombre de la variedad del vino, por ejemplo Fino, el porcentaje de alcohol, por ejemplo 15%, y la capacidad 75cl.
• La etiqueta trasera debe incluir el logo oficial Sellora del Consejo, y cuatro logos adicionales con una dimension menor. El Logo de ¨Europa invierte en las zonas rurales¨ debe ser de mayor tamaño que los otros. Se precisa espacio para el texto descriptivo de los vinos.
• Las dimensiones de la botella se puede encontrar en este enlace
• http://www.vidrialto.example/es/catalogo/vinos-y-espumosos/bordelesas/bd-orla
• Altura:305 mm
• Diámetro base:76,20 mm
• Diámetro hombro:82 mm
• Tipo boca:Cetie
• Peso:750 gr
• Capacidad:75 cl
Nice to have
• See our website velmora-vinos.example to understand the origin of the wines. Ver nuestra página web velmora-vinos.example para mejor entender los vinos.
Should not have
• Images of catavinos or stereotypical images from Spain such as flamenco dancers or guitars.

```html
<!DOCTYPE html>
<html lang="es">
<head>
<meta charset="utf-8">
<title>Vinos de Albarrán – Etiquetas</title>
<link rel="stylesheet" href="https://fonts.googleapis.com/css2?family=Cormorant+Garamond:wght@500&family=Libre+Baskerville:ital@1&family=Montserrat:wght@500;700&display=swap">
<style>
  :root {
    --board: #f2f2f2;
    --ink: #1a1a1a;
    --label-black: #0b0b0b;
    --white: #ffffff;
    --amontillado-red: #c4161c;
    --manzanilla-yellow: #e8c44e;
    --medium-orange: #f7a12c;
    --rule: #9a9a9a;
  }
  * { margin: 0; padding: 0; box-sizing: border-box; }
  html, body { width: 1200px; height: 1200px; overflow: hidden; background: var(--board); }
  .board { position: relative; width: 1200px; height: 1200px; }

  .brand { position: absolute; left: 86px; top: 196px; width: 220px; text-align: center;
    font-family: "Cormorant Garamond", serif; font-weight: 500; color: var(--ink); }
  .brand-name { font-size: 30px; letter-spacing: -0.5px; line-height: 1; }
  .brand-tagline { margin-top: 12px; font-size: 13px; letter-spacing: 3px; }

  .swatches { position: absolute; left: 110px; top: 302px; display: flex; gap: 17px; }
  .swatch { width: 45px; height: 45px; }
  .swatch--red { background: var(--amontillado-red); }
  .swatch--yellow { background: var(--manzanilla-yellow); }
  .swatch--orange { background: var(--medium-orange); }

  .label { position: absolute; display: block; }
  .capsule { position: absolute; width: 48px; height: 104px; border-radius: 3px 3px 0 0; }
  .capsule--red { background: linear-gradient(90deg, #a31015, var(--amontillado-red) 45%, #a31015); }
  .capsule--yellow { background: linear-gradient(90deg, #c9a73c, var(--manzanilla-yellow) 45%, #c9a73c); }
  .capsule--orange { background: linear-gradient(90deg, #d8861d, var(--medium-orange) 45%, #d8861d); }

  .divider { position: absolute; left: 22px; right: 22px; top: 1165px; border-top: 1px dashed var(--rule); }

  .t-serif { font-family: "Cormorant Garamond", serif; font-weight: 500; }
  .t-sans { font-family: "Montserrat", sans-serif; font-weight: 500; }
  .t-sans-bold { font-family: "Montserrat", sans-serif; font-weight: 700; }
  .t-italic { font-family: "Libre Baskerville", serif; font-style: italic; }
  .fill-black { fill: var(--label-black); }
  .fill-white { fill: var(--white); }
  .fill-red { fill: var(--amontillado-red); }
  .fill-yellow { fill: var(--manzanilla-yellow); }
  .fill-orange { fill: var(--medium-orange); }
</style>
</head>
<body>
<div class="board">

  <svg width="0" height="0" style="position:absolute" aria-hidden="true">
    <defs>
      <symbol id="front-base" viewBox="0 0 110 414">
        <rect width="110" height="414" class="fill-black"/>
        <text x="55" y="36" text-anchor="middle" class="t-serif fill-white" font-size="15" letter-spacing="1.5">ALBARRÁN</text>
        <text x="55" y="88" text-anchor="middle" class="t-serif fill-white" font-size="6.5">DENOMINACIONES</text>
        <text x="55" y="95" text-anchor="middle" class="t-serif fill-white" font-size="6.5">DE ORIGEN</text>
        <line x1="57" y1="150" x2="57" y2="396" stroke="#fff" stroke-width="0.6"/>
        <text transform="translate(52,200) rotate(-90)" class="t-sans-bold fill-white" font-size="6.5">75 cl  |  19% vol</text>
        <text transform="translate(30,396) rotate(-90)" class="t-italic fill-white" font-size="5.6">
          <tspan x="0" dy="0">Vino seleccionado por el</tspan>
          <tspan x="0" dy="7">CONSEJO REGULADOR</tspan>
          <tspan x="0" dy="7">de la Denominación de Origen</tspan>
        </text>
      </symbol>

      <symbol id="back-base" viewBox="0 0 110 414">
        <rect width="110" height="414" class="fill-black"/>
        <text x="55" y="28" text-anchor="middle" class="t-serif fill-white" font-size="11" letter-spacing="1">ALBARRÁN</text>
        <text x="55" y="79" text-anchor="middle" class="t-serif fill-white" font-size="4.5">DENOMINACIONES DE ORIGEN</text>
        <rect x="12" y="110" width="26" height="66" rx="2" class="fill-white" role="img" aria-label="Sello de socio"/>
        <circle cx="24" cy="262" r="10" fill="none" stroke="#fff" stroke-width="1.2" role="img" aria-label="Sello del Consejo"/>
        <rect x="14" y="298" width="20" height="26" rx="2" class="fill-white" role="img" aria-label="Sello institucional"/>
        <rect x="10" y="344" width="28" height="36" class="fill-white" role="img" aria-label="Sello europeo"/>
      </symbol>

      <symbol id="front-amontillado" viewBox="0 0 110 414">
        <use href="#front-base"/>
        <circle cx="55" cy="60" r="11" class="fill-red"/>
        <rect x="62" y="123" width="24" height="273" class="fill-red"/>
        <text transform="translate(79,388) rotate(-90)" class="t-sans fill-white" font-size="10" letter-spacing="1">AMONTILLADO</text>
      </symbol>
      <symbol id="front-manzanilla" viewBox="0 0 110 414">
        <use href="#front-base"/>
        <circle cx="55" cy="60" r="11" class="fill-yellow"/>
        <rect x="62" y="123" width="24" height="273" class="fill-yellow"/>
        <text transform="translate(79,388) rotate(-90)" class="t-sans fill-white" font-size="10" letter-spacing="1">MANZANILLA</text>
      </symbol>
      <symbol id="front-medium" viewBox="0 0 110 414">
        <use href="#front-base"/>
        <circle cx="55" cy="60" r="11" class="fill-orange"/>
        <rect x="62" y="123" width="24" height="273" class="fill-orange"/>
        <text transform="translate(79,388) rotate(-90)" class="t-sans fill-white" font-size="10" letter-spacing="1">MEDIUM</text>
      </symbol>

      <symbol id="back-amontillado" viewBox="0 0 110 414">
        <use href="#back-base"/>
        <circle cx="55" cy="48" r="8" class="fill-red"/>
        <text x="55" y="70" text-anchor="middle" class="t-sans-bold fill-white" font-size="4.6" letter-spacing="1">AMONTILLADO</text>
        <rect x="37" y="83" width="36" height="6" class="fill-red"/>
        <text transform="translate(64,396) rotate(-90)" class="t-italic fill-white" font-size="4.3">
          <tspan x="0" dy="0">El AMONTILLADO es un vino muy singular, que combina la crianza bajo velo de flor, propia</tspan>
          <tspan x="0" dy="5.6">del Fino y la Manzanilla, con un periodo posterior en el que el velo de flor desaparece y el</tspan>
          <tspan x="0" dy="5.6">vino se expone a la oxidación. Elaborados con uva palomino, son los Amontillados</tspan>
          <tspan x="0" dy="5.6">vinos extraordinariamente complejos e interesantes.</tspan>
        </text>
      </symbol>
      <symbol id="back-manzanilla" viewBox="0 0 110 414">
        <use href="#back-base"/>
        <circle cx="55" cy="48" r="8" class="fill-yellow"/>
        <text x="55" y="70" text-anchor="middle" class="t-sans-bold fill-white" font-size="4.6" letter-spacing="1">MANZANILLA</text>
        <rect x="37" y="83" width="36" height="6" class="fill-yellow"/>
        <text transform="translate(64,396) rotate(-90)" class="t-italic fill-white" font-size="4.3">
          <tspan x="0" dy="0">La MANZANILLA es un vino blanco y seco, criado bajo velo de flor en bodegas</tspan>
          <tspan x="0" dy="5.6">junto al mar, de color pajizo y aroma punzante con notas salinas y de camomila.</tspan>
          <tspan x="0" dy="5.6">Ligera y fresca en boca, ideal con mariscos y pescados.</tspan>
        </text>
      </symbol>
      <symbol id="back-medium" viewBox="0 0 110 414">
        <use href="#back-base"/>
        <circle cx="55" cy="48" r="8" class="fill-orange"/>
        <text x="55" y="70" text-anchor="middle" class="t-sans-bold fill-white" font-size="4.6" letter-spacing="1">MEDIUM</text>
        <rect x="37" y="83" width="36" height="6" class="fill-orange"/>
        <text transform="translate(64,396) rotate(-90)" class="t-italic fill-white" font-size="4.3">
          <tspan x="0" dy="0">El MEDIUM nace del ensamblaje de un vino seco con un vino dulce natural,</tspan>
          <tspan x="0" dy="5.6">de color ámbar y aroma a frutos secos y pasas. En boca resulta suave y</tspan>
          <tspan x="0" dy="5.6">equilibrado, perfecto como aperitivo.</tspan>
        </text>
      </symbol>
    </defs>
  </svg>

  <header class="brand">
    <div class="brand-name">VINOS DE ALBARRÁN</div>
    <div class="brand-tagline">VELMORA WINES</div>
  </header>

  <div class="swatches">
    <div class="swatch swatch--red"></div>
    <div class="swatch swatch--yellow"></div>
    <div class="swatch swatch--orange"></div>
  </div>

  <!-- Amontillado front and back, full size -->
  <svg class="label" style="left:400px;top:48px" width="110" height="414" viewBox="0 0 110 414"><use href="#front-amontillado"/></svg>
  <svg class="label" style="left:518px;top:48px" width="110" height="414" viewBox="0 0 110 414"><use href="#back-amontillado"/></svg>

  <!-- Other varieties, front labels -->
  <svg class="label" style="left:760px;top:48px" width="110" height="414" viewBox="0 0 110 414"><use href="#front-manzanilla"/></svg>
  <svg class="label" style="left:920px;top:48px" width="110" height="414" viewBox="0 0 110 414"><use href="#front-medium"/></svg>

  <!-- Capsules and labels per variety -->
  <div class="capsule capsule--red" role="img" aria-label="Cápsula roja con motivo de la marca" style="left:184px;top:560px"></div>
  <div class="capsule capsule--red" role="img" aria-label="Cápsula roja con motivo de la marca" style="left:342px;top:560px"></div>
  <div class="capsule capsule--yellow" role="img" aria-label="Cápsula amarilla con motivo de la marca" style="left:500px;top:560px"></div>
  <div class="capsule capsule--yellow" role="img" aria-label="Cápsula amarilla con motivo de la marca" style="left:658px;top:560px"></div>
  <div class="capsule capsule--orange" role="img" aria-label="Cápsula naranja con motivo de la marca" style="left:816px;top:560px"></div>
  <div class="capsule capsule--orange" role="img" aria-label="Cápsula naranja con motivo de la marca" style="left:974px;top:560px"></div>

  <svg class="label" style="left:176px;top:775px" width="64" height="241" viewBox="0 0 110 414"><use href="#front-amontillado"/></svg>
  <svg class="label" style="left:334px;top:775px" width="64" height="241" viewBox="0 0 110 414"><use href="#back-amontillado"/></svg>
  <svg class="label" style="left:492px;top:775px" width="64" height="241" viewBox="0 0 110 414"><use href="#front-manzanilla"/></svg>
  <svg class="label" style="left:650px;top:775px" width="64" height="241" viewBox="0 0 110 414"><use href="#back-manzanilla"/></svg>
  <svg class="label" style="left:808px;top:775px" width="64" height="241" viewBox="0 0 110 414"><use href="#front-medium"/></svg>
  <svg class="label" style="left:966px;top:775px" width="64" height="241" viewBox="0 0 110 414"><use href="#back-medium"/></svg>

  <div class="divider"></div>
</div>
</body>
</html>
```